New Business Card for our Indoor Golf Training Facility

We are looking for designs for a new business card for our indoor golf training facility. Attached is our logo, our logo with our slogan, and here is our elevator pitch (What makes us different from the others) not sure if all the info will fit on one card, maybe you can condense the elevator pitch? here is the info

Elevator Pitch
We work with serious golfers and those that want to be serious golfers…
to make you better, faster, at all phases of the game…
We use the same state-of-the-art technology as professional golfers…
which produces data sets that shows your improvement in real time.
Our facility is available 24/7 to our members, which allows you to improve on your time.

our website: www.brambleteegolf.com

Target Market(s)

Golfers

Font styles to use
Serif
Sans Serif

Colors
ec1f27
f59195
fbd4d5
919191
d3d3d3
1b1b1b

Requirements
Must have
• our logo or our logo with the slogan, elevator pitch (can be condensed or shortened)

```html
<!DOCTYPE html>
<html lang="en">
<head>
<meta charset="utf-8">
<title>Bramble Tee Golf – Business Card</title>
<link href="https://fonts.googleapis.com/css2?family=Roboto:wght@400;500;700;900&display=swap" rel="stylesheet">
<style>
  :root {
    --brand-red: #ec1f27;
    --card-red: #e9463b;
    --pink: #f59195;
    --blush: #fbd4d5;
    --mid-grey: #919191;
    --light-grey: #d3d3d3;
    --ink: #1b1b1b;
    --paper: #f3f3f3;
    --stage: #2a2a2a;
    --white: #ffffff;
  }
  html, body {
    margin: 0;
    padding: 0;
    width: 1200px;
    height: 886px;
    overflow: hidden;
    background: var(--stage);
    font-family: "Roboto", Arial, sans-serif;
  }
  .canvas {
    position: relative;
    width: 1200px;
    height: 886px;
  }
  .card {
    position: absolute;
    width: 560px;
    height: 320px;
    border-radius: 18px;
    overflow: hidden;
    box-shadow: 0 14px 30px rgba(0,0,0,0.45);
  }

  /* Back of card */
  .card-back {
    left: 60px;
    top: 90px;
    background: var(--card-red);
    color: var(--white);
    text-align: center;
  }
  .back-mark {
    display: flex;
    align-items: center;
    justify-content: center;
    gap: 12px;
    margin-top: 48px;
  }
  .back-mark .ring {
    width: 52px;
    height: 52px;
    border: 5px solid var(--white);
    border-radius: 50%;
    box-sizing: border-box;
  }
  .back-mark .brand-name {
    font-size: 28px;
    font-weight: 700;
    color: var(--white);
    white-space: nowrap;
  }
  .pitch-title {
    margin: 28px 0 8px;
    font-size: 17px;
    font-weight: 700;
    letter-spacing: 0.5px;
  }
  .pitch-text {
    margin: 0 30px;
    font-size: 12.5px;
    line-height: 1.45;
    font-weight: 500;
  }

  /* Front of card */
  .card-front {
    left: 580px;
    top: 476px;
    background: var(--paper);
  }
  .front-logo {
    position: absolute;
    left: 26px;
    top: 100px;
  }
  .front-logo .logo-row {
    display: flex;
    align-items: center;
    gap: 10px;
  }
  .front-logo .ring {
    width: 42px;
    height: 42px;
    border: 3px solid var(--brand-red);
    border-radius: 50%;
    box-sizing: border-box;
    flex: none;
  }
  .front-logo .brand-name {
    font-size: 23px;
    font-weight: 900;
    color: var(--brand-red);
    line-height: 1;
    white-space: nowrap;
  }
  .front-logo .slogan {
    margin: 2px 0 0 52px;
    font-size: 10px;
    color: var(--brand-red);
    white-space: nowrap;
  }
  .divider {
    position: absolute;
    left: 290px;
    top: 70px;
    width: 1.5px;
    height: 120px;
    background: var(--mid-grey);
  }
  .contact {
    position: absolute;
    left: 306px;
    top: 78px;
    color: var(--ink);
  }
  .contact .person-name {
    font-size: 22px;
    font-weight: 700;
    color: var(--brand-red);
    letter-spacing: 0.5px;
    line-height: 1;
    white-space: nowrap;
  }
  .contact .person-role {
    font-size: 14px;
    font-weight: 700;
    margin: 3px 0 10px;
  }
  .contact .address {
    font-size: 14px;
    line-height: 1.3;
    margin-bottom: 6px;
    white-space: nowrap;
  }
  .contact .line {
    display: flex;
    align-items: center;
    gap: 8px;
    font-size: 14px;
    line-height: 1.45;
    white-space: nowrap;
  }
  .contact .line svg {
    width: 12px;
    height: 12px;
    fill: var(--brand-red);
    flex: none;
  }
  .footer-band {
    position: absolute;
    left: 0;
    bottom: 0;
    width: 560px;
    height: 70px;
  }
  .website {
    position: absolute;
    left: 18px;
    bottom: 20px;
    font-size: 14px;
    color: var(--white);
    letter-spacing: 3.5px;
    white-space: nowrap;
  }
</style>
</head>
<body>
<div class="canvas">

  <section class="card card-back">
    <div class="back-mark">
      <span class="ring"></span>
      <span class="brand-name">Bramble Tee Golf</span>
    </div>
    <h2 class="pitch-title">ELEVATOR PITCH :</h2>
    <p class="pitch-text">
      Indoor golf training for players of every level, from beginner to scratch…<br>
      built to sharpen your swing, your short game and your putting…<br>
      Our simulators and launch monitors track every shot you hit…<br>
      so you see clear numbers on your progress after each session.<br>
      Members get round-the-clock access, so you can practice whenever suits you.
    </p>
  </section>

  <section class="card card-front">
    <div class="front-logo">
      <div class="logo-row">
        <span class="ring"></span>
        <span class="brand-name">Bramble Tee Golf</span>
      </div>
      <div class="slogan">Swing Smarter. Score Lower. Play Often.</div>
    </div>

    <div class="divider"></div>

    <div class="contact">
      <div class="person-name">DANA WHITFIELD</div>
      <div class="person-role">CEO/FOUNDER</div>
      <div class="address">1480 W. Larch Rd. Unit B4<br>Millbrook, OH 45099</div>
      <div class="line">
        <svg viewBox="0 0 24 24" aria-hidden="true"><path d="M6.6 10.8a15.1 15.1 0 0 0 6.6 6.6l2.2-2.2a1 1 0 0 1 1-.25 11.4 11.4 0 0 0 3.6.57 1 1 0 0 1 1 1V20a1 1 0 0 1-1 1A17 17 0 0 1 3 4a1 1 0 0 1 1-1h3.5a1 1 0 0 1 1 1c0 1.25.2 2.45.57 3.57a1 1 0 0 1-.25 1z"/></svg>
        <span>555-210-3380</span>
      </div>
      <div class="line">
        <svg viewBox="0 0 24 24" aria-hidden="true"><path d="M2 5h20v14H2z M3 6l9 7 9-7" fill="none" stroke="#ec1f27" stroke-width="2.4"/></svg>
        <span>info@brambleteegolf.com</span>
      </div>
    </div>

    <svg class="footer-band" viewBox="0 0 560 70" preserveAspectRatio="none" aria-hidden="true">
      <polygon points="0,8 262,8 292,70 0,70" fill="var(--card-red)"/>
      <polygon points="276,36 560,50 560,70 292,70" fill="var(--mid-grey)"/>
      <polygon points="286,56 560,60 560,70 292,70" fill="var(--card-red)"/>
    </svg>
    <div class="website">www.brambleteegolf.com</div>
  </section>

</div>
</body>
</html>
```